Book title: Wildflower: The gift of stillness!

This book is called: Wildflower: The gift of stillness!

A guide to understanding the most popular types of coaching and how to find the perfect coach for you.
The coaching industry has exploded over the past few years as the demand for them has increased. With so many different types of coaches it can be intimidating and overwhelming to find the perfect one for you. To further complicate matters, you may experience times in your life when you require multiple coaches. {Book Title} aims to quite the noise and assist you in finding the perfect coach for you. In this book, you will learn more about the different types of coaching as well as meet a hand-picked selection of coaches from the most popular coaching niches. Each featured coach has provided an exercise designed to move you powerfully forward. We encourage you to work through each exercise so you may experience firsthand the power of working with these incredible coaches.

We would like a professional and simple design. See examples included. We would like to see blood orange included in the design, please see color pallets included as well.

Target Market(s)

Corporate professionals wanting to explore the various types of coaching industry

Industry/Entity Type

Coaching - Health, business, spiritual

Font styles to use
Serif

Colors
EE7325
F08F49
F5BC92
FAE3D3
FDF4ED

Requirements
Must have
• Please include book title: Wildflower, Subtitle: The gift of stillness! Name of publishing company: Silver Lantern Publishing, Spaces for 8 author names on the front of the cover- Author Name
Nice to have
• A feminine yet corporate feel.
Should not have
• We don't want it

```html
<!DOCTYPE html>
<html lang="en">
<head>
<meta charset="utf-8">
<title>Wildflower: The gift of stillness!</title>
<link rel="stylesheet" href="https://fonts.googleapis.com/css2?family=Cinzel:wght@400;500;600&family=EB+Garamond:wght@400&display=swap">
<style>
  :root {
    --paper: #ffffff;
    --sage: #8fab99;
    --blood-orange: #ff522b;
    --ink: #5e5a5c;
    --author-grey: #9b9a9a;
  }
  * { margin: 0; padding: 0; box-sizing: border-box; }
  html, body { width: 800px; height: 1200px; overflow: hidden; background: var(--paper); }
  .cover {
    position: relative;
    width: 800px;
    height: 1200px;
    background: var(--paper);
    font-family: "Cinzel", serif;
    overflow: hidden;
  }
  .line {
    position: absolute;
    left: 0;
    width: 100%;
    text-align: center;
    line-height: 1;
    white-space: nowrap;
  }
  .rings { position: absolute; left: 0; top: 0; width: 800px; height: 1200px; }
  .publisher {
    top: 38px;
    font-size: 28px;
    font-weight: 400;
    color: var(--sage);
    letter-spacing: 0.36em;
    padding-left: 0.36em;
  }
  .title {
    top: 250px;
    font-size: 52px;
    font-weight: 500;
    color: var(--sage);
    letter-spacing: 0.42em;
    padding-left: 0.42em;
  }
  .subtitle-lead {
    top: 347px;
    font-size: 42px;
    font-weight: 400;
    color: var(--blood-orange);
    letter-spacing: 0.38em;
    padding-left: 0.38em;
  }
  .subtitle-main {
    top: 430px;
    font-size: 112px;
    font-weight: 400;
    color: var(--blood-orange);
    letter-spacing: 0.01em;
  }
  .tagline {
    top: 752px;
    font-size: 27px;
    font-weight: 600;
    color: var(--blood-orange);
    line-height: 33px;
  }
  .promise-lead {
    top: 840px;
    font-size: 27px;
    color: var(--ink);
  }
  .promise-main {
    top: 870px;
    font-size: 41px;
    color: var(--ink);
  }
  .authors {
    top: 1022px;
    font-family: "EB Garamond", serif;
    font-size: 31px;
    color: var(--author-grey);
    line-height: 46px;
  }
</style>
</head>
<body>
  <main class="cover">
    <svg class="rings" viewBox="0 0 800 1200" aria-hidden="true">
      <ellipse cx="402" cy="398" rx="270" ry="283" fill="none" stroke="#8fab99" stroke-width="2" transform="rotate(-12 402 398)"/>
      <ellipse cx="408" cy="403" rx="283" ry="265" fill="none" stroke="#8fab99" stroke-width="2" transform="rotate(18 408 403)"/>
    </svg>

    <p class="line publisher">Silver Lantern Publishing</p>

    <h1 class="line title">Wildflower</h1>
    <h2 class="line subtitle-lead">The Gift of</h2>
    <h2 class="line subtitle-main">STILLNESS</h2>

    <p class="line tagline">A GUIDE TO UNDERSTANDING<br>THE MOST POPULAR TYPES OF COACHING</p>
    <p class="line promise-lead">AND HOW TO FIND</p>
    <p class="line promise-main">THE PERFECT COACH FOR YOU</p>

    <p class="line authors">Author Name 1, Author Name 2, Author Name 3<br>Author Name 4, Author Name 5, Author Name 6<br>Author Name 7, Author Name 8</p>
  </main>
</body>
</html>
```